Treet Friends/Pebble Feast

Create a double sided postcard which will be distributed to 60,000 destinations, suitable for printing on re-cycled card.

Promotional offer ends Sunday August 31st 2014

It is Winter in Perth Western Australia, colours need to be bright and a reminder of summer. The card needs to be fun with a Mediterranean Spanish type feel
web site www.korlinde.com.au

```html
<!DOCTYPE html>
<html lang="en">
<head>
<meta charset="utf-8">
<title>Pebble Feast Postcard</title>
<link rel="stylesheet" href="https://fonts.googleapis.com/css2?family=Arimo:wght@400;700&display=swap">
<style>
  :root {
    --brand-blue: #1f63ad;
    --paper: #ffffff;
    --ink: #1a1a1a;
    --ink-soft: #333333;
    --backdrop: #e9e6e1;
    --rule: #222222;
    --stamp: #111111;
  }
  * { box-sizing: border-box; margin: 0; padding: 0; }
  html, body { width: 1200px; height: 733px; overflow: hidden; }
  body {
    background: var(--backdrop);
    font-family: "Arimo", Arial, sans-serif;
    color: var(--ink);
    position: relative;
  }
  .card {
    position: absolute;
    background: var(--paper);
    box-shadow: 0 2px 6px rgba(0,0,0,.25);
    overflow: hidden;
  }
  .card--front { left: 41px; top: 75px; width: 480px; height: 620px; }
  .card--back { left: 540px; top: 145px; width: 618px; height: 482px; }

  /* front */
  .front-header {
    position: absolute; left: 0; top: 0; width: 480px; height: 87px;
    background: var(--brand-blue); color: var(--paper); text-align: center;
  }
  .front-header__title { font-size: 24px; font-weight: 400; padding-top: 15px; }
  .front-header__intro { font-size: 12px; font-weight: 700; line-height: 16px; margin-top: 7px; }
  .hero-photo {
    position: absolute; left: 0; top: 87px; width: 480px; height: 246px;
    background: radial-gradient(ellipse at 55% 55%, #e08a5c 0%, #d9c6b4 35%, #eae6e1 65%, #c9c2b9 100%);
  }
  .offer-band {
    position: absolute; left: 0; top: 333px; width: 480px; height: 107px;
    background: var(--brand-blue); color: var(--paper); text-align: center;
  }
  .offer-band__price-line { font-size: 23px; padding-top: 22px; }
  .offer-band__price { font-size: 35px; font-weight: 700; }
  .offer-band__details { font-size: 12px; margin-top: 14px; }
  .photo-strip { position: absolute; top: 443px; height: 97px; }
  .photo-strip--salmon { left: 0; width: 152px; background: linear-gradient(135deg, #3a3a36, #c8754f 60%, #e2a07b); }
  .photo-strip--harbour { left: 164px; width: 150px; background: linear-gradient(180deg, #b9c4cc 0%, #8ea3b3 55%, #4b5863 100%); }
  .photo-strip--diners { left: 317px; width: 163px; background: linear-gradient(135deg, #2b1a10, #7a4a2a 55%, #c08a5a); }
  .front-footer { position: absolute; left: 0; top: 540px; width: 480px; height: 80px; }
  .brand-mark {
    position: absolute; background: var(--brand-blue); color: var(--paper);
    display: flex; align-items: center; justify-content: center;
    font-weight: 700; letter-spacing: 2px;
  }
  .front-footer .brand-mark { left: 15px; top: 6px; width: 119px; height: 58px; font-size: 13px; }
  .contact { position: absolute; color: var(--ink-soft); }
  .contact__bookings { font-size: 15px; }
  .contact__address { font-size: 9.5px; color: var(--ink); margin-top: 2px; }
  .front-footer .contact { left: 147px; top: 21px; }
  .conditions { position: absolute; right: 14px; top: 61px; font-size: 9px; }

  /* back */
  .back-header {
    position: absolute; left: 0; top: 0; width: 465px; height: 155px;
    background: var(--brand-blue); color: var(--paper); text-align: center;
  }
  .back-header__title { font-size: 23px; line-height: 30px; padding-top: 12px; }
  .back-header__price { font-size: 30px; font-weight: 700; margin-top: 5px; }
  .back-header__hours { font-size: 15px; margin-top: 14px; }
  .stamp-box { position: absolute; left: 473px; top: 20px; width: 122px; height: 126px; background: var(--stamp); }
  .menu {
    position: absolute; left: 0; top: 165px; width: 311px;
    text-align: center; font-size: 9.6px; line-height: 12.4px;
  }
  .divider-v { position: absolute; left: 310px; top: 155px; width: 1px; height: 260px; background: var(--rule); }
  .divider-h { position: absolute; left: 0; top: 416px; width: 618px; height: 1px; background: var(--rule); }
  .address-lines { position: absolute; left: 368px; top: 228px; font-size: 10px; }
  .address-line { position: absolute; left: 20px; width: 168px; height: 1px; background: var(--ink-soft); }
  .back-footer .brand-mark { left: 13px; top: 421px; width: 94px; height: 46px; font-size: 11px; }
  .back-footer .contact { left: 205px; top: 429px; }
</style>
</head>
<body>

<section class="card card--front">
  <header class="front-header">
    <h1 class="front-header__title">Celebrate Pebble Feast’s</h1>
    <p class="front-header__intro">Celebrate Sunday’s on Perth’s most beautiful bay with a selection of magnificent<br>Western Australian seafood, from Shark Bay.</p>
  </header>
  <div class="hero-photo" role="img" aria-label="Bowl of seafood stew with prawns and a mound of rice"></div>
  <div class="offer-band">
    <p class="offer-band__price-line">Pebble Feast Plate <span class="offer-band__price">$38.00</span>pp</p>
    <p class="offer-band__details">Grilled Scampi, Prawns, Cuttlefish, Pink Snapper and Scallops</p>
  </div>
  <div class="photo-strip photo-strip--salmon" role="img" aria-label="Cured salmon plated with a side salad"></div>
  <div class="photo-strip photo-strip--harbour" role="img" aria-label="Harbour with moored yachts and city skyline"></div>
  <div class="photo-strip photo-strip--diners" role="img" aria-label="Couple enjoying wine at a candlelit table"></div>
  <footer class="front-footer">
    <div class="brand-mark">KORLINDE</div>
    <div class="contact">
      <p class="contact__bookings">Bookings w: www.korlinde.com.au p 9400-7182</p>
      <p class="contact__address">Korlinde Restaurant and Function Centre 8 Wattle Parade Crawley 6009</p>
    </div>
    <p class="conditions">Conditions apply: not available in conjunction with any other offer</p>
  </footer>
</section>

<section class="card card--back">
  <header class="back-header">
    <h2 class="back-header__title">Reward yourself with Lunch overlooking<br>Perth’s most beautiful Bay</h2>
    <p class="back-header__price">$48.00 per person</p>
    <p class="back-header__hours">(Available Monday to Friday 11am until 3pm)</p>
  </header>
  <div class="stamp-box"></div>
  <div class="menu">
    Select one dish from each course with your choice of either a glass<br>
    of Corvetto Soave 2011 or Villa Lunetta Valpolicella Classico 2011<br>
    Freshly baked Italian style crusty bread,<br>
    Entrée<br>
    Passionfruit and citrus cured Tasmanian salmon<br>
    or<br>
    Pork belly, marinated, horseradish coleslaw<br>
    or<br>
    Welsh rarebit, sautéed mushrooms, hot English mustard mayo<br>
    or<br>
    Fried squid, tubes, cannellini pure, green chilli sauce<br>
    Main<br>
    Pink snapper fillet, grilled, xo sauce, kim chi<br>
    or<br>
    Wagyu rump, served with cauliflower puree, broad beans<br>
    or<br>
    Soft polenta, grilled haloumi, crusted eggplant, red pepper coulis<br>
    or<br>
    Confit duck leg caramelised red onion, grilled manchego stuffed fig
  </div>
  <div class="divider-v"></div>
  <div class="address-lines">
    <span>To,</span>
    <div class="address-line" style="top:10px"></div>
    <div class="address-line" style="top:39px"></div>
    <div class="address-line" style="top:68px"></div>
    <div class="address-line" style="top:97px"></div>
  </div>
  <div class="divider-h"></div>
  <footer class="back-footer">
    <div class="brand-mark">KORLINDE</div>
    <div class="contact">
      <p class="contact__bookings">Bookings w: www.korlinde.com.au p 9400-7182</p>
      <p class="contact__address">Korlinde Restaurant and Function Centre 8 Wattle Parade Crawley 6009</p>
    </div>
  </footer>
</section>

</body>
</html>
```